Tattoo Shop Business Card

I need a Business Card for the The Harbor Quill.

I'm thinking i want a double sided business card, really clean, very classy, one side the logo, and on the other my information. I'm pretty much open to anything, as long as its fun and captures class and elegance, while at the same time is edgy and tattooish.
I don't want your typical classic card. Add your own twist on it

Logo is attached to this brief

Please include:
Name
Position
Phone Number
Email
Website

Target Market(s)

I'm looking to capture potential clients for my tattoo shop so the card needs to be something they can fit in their wallet but they will also remember me when they see that card in there. My target audience is everyone over 18 that is intrigued by tattoos and piercings.

Industry/Entity Type

Business

Font styles to use
Serif

Colors

Designer to choose colors to be used in the design.

Requirements
Must have
• must be bold and something people will never forget

```html
<!DOCTYPE html>
<html lang="en">
<head>
<meta charset="utf-8">
<title>The Harbor Quill – Business Card</title>
<link href="https://fonts.googleapis.com/css2?family=Libre+Baskerville:wght@400;700&display=swap" rel="stylesheet">
<style>
  :root {
    --page: #e9e6e1;
    --card-dark: #2a2424;
    --card-dark-edge: #1d1919;
    --card-light: #f7f7f7;
    --ink-light: #f2efea;
    --ink-muted: #cfc9c2;
    --ink-dark: #2a2424;
    --strip: #e4e4e4;
  }
  * { box-sizing: border-box; margin: 0; padding: 0; }
  html, body { width: 1200px; height: 886px; overflow: hidden; }
  body {
    background: var(--page);
    font-family: "Libre Baskerville", Georgia, serif;
    display: flex;
    flex-direction: column;
    align-items: center;
    justify-content: center;
    gap: 56px;
  }
  .card {
    position: relative;
    width: 600px;
    height: 343px;
    border-radius: 22px;
    overflow: hidden;
    box-shadow: 0 10px 24px rgba(0,0,0,0.18);
  }
  .card--info {
    background: var(--card-dark);
    color: var(--ink-light);
    padding: 44px 80px 0 56px;
  }
  .card--info .edge-strip {
    position: absolute;
    top: 0; right: 0; bottom: 0;
    width: 26px;
    background: var(--strip);
  }
  .brand-name {
    font-weight: 700;
    font-size: 42px;
    letter-spacing: 0.02em;
    line-height: 1;
  }
  .card--info .brand-name { color: var(--ink-light); }
  .person {
    margin-top: 30px;
  }
  .person-name {
    font-size: 24px;
    line-height: 1.1;
  }
  .person-role {
    font-size: 14px;
    color: var(--ink-muted);
    margin-top: 6px;
    padding-top: 6px;
    border-top: 1px solid var(--ink-muted);
    display: inline-block;
  }
  .contact {
    list-style: none;
    margin-top: 22px;
    font-size: 15px;
    line-height: 1.75;
  }
  .rule {
    position: absolute;
    left: 56px;
    right: 80px;
    bottom: 30px;
    height: 1px;
    background: var(--ink-muted);
  }
  .card--logo {
    background: linear-gradient(135deg, #ffffff 0%, var(--card-light) 55%, #e6e6e6 100%);
    display: flex;
    align-items: center;
    justify-content: center;
  }
  .card--logo .brand-name {
    color: var(--ink-dark);
    font-size: 50px;
  }
</style>
</head>
<body>
  <section class="card card--info" aria-label="Card back: contact details">
    <p class="brand-name">The Harbor Quill</p>
    <div class="person">
      <p class="person-name">Employee Name</p>
      <p class="person-role">Managing Director</p>
    </div>
    <ul class="contact">
      <li>0012 3456 789</li>
      <li>info@youremail.com</li>
      <li>www.yourwebsite.com</li>
    </ul>
    <div class="rule"></div>
    <div class="edge-strip"></div>
  </section>

  <section class="card card--logo" aria-label="Card front: shop name">
    <p class="brand-name">The Harbor Quill</p>
  </section>
</body>
</html>
```